VelmoraMD is an aesthetics and wellness medical spa. I am looking for a modern site, not too glam, not too boring. Currently I have the coming soon page at velmoraMD.com. The green in the logo is the accent color. I need the site to be semi neutral. I don't want it to be too geared towards females because there are some consults that men also will participate in.

```html
<!DOCTYPE html>
<html lang="en">
<head>
<meta charset="utf-8">
<title>VelmoraMD — Aesthetics &amp; Wellness</title>
<link href="https://fonts.googleapis.com/css2?family=Lato:ital,wght@0,300;0,400;0,700;1,400&display=swap" rel="stylesheet">
<style>
:root{
  --mint:#a8d3c1;
  --mint-deep:#8cc2ab;
  --ink:#1e1e1e;
  --text:#444;
  --muted:#777;
  --soft-bg:#f2f2f2;
  --footer:#1f1f1f;
  --white:#fff;
}
*{box-sizing:border-box;margin:0;padding:0}
html,body{width:1200px;height:4214px;overflow:hidden}
body{font-family:'Lato',sans-serif;color:var(--text);background:var(--white);position:relative}
.abs{position:absolute}
.accent-bar{position:absolute;width:44px;height:5px;border-radius:3px;background:var(--mint)}

.top-bar{position:absolute;top:0;left:0;width:1200px;height:36px;background:var(--mint);color:var(--white);font-size:16px;display:flex;align-items:center;justify-content:center;gap:10px}
.top-bar svg{width:13px;height:13px;fill:var(--white);vertical-align:-1px;margin-right:4px}

.site-header{position:absolute;top:36px;left:0;width:1200px;height:112px;background:var(--white)}
.brand{position:absolute;left:106px;top:30px;font-size:44px;font-weight:700;color:var(--ink);letter-spacing:-0.5px}
.main-nav{position:absolute;left:487px;top:44px;display:flex;gap:21px;font-size:17px;color:var(--ink)}
.main-nav .current{color:var(--mint-deep)}
.btn-outline{position:absolute;border:1.5px solid #555;background:transparent;color:var(--ink);font-size:17px;display:flex;align-items:center;justify-content:center;text-transform:uppercase}
.btn-white{position:absolute;background:var(--white);color:var(--ink);font-size:19px;display:flex;align-items:center;justify-content:center;text-transform:uppercase}

.hero{position:absolute;top:148px;left:0;width:1200px;height:622px;background:linear-gradient(100deg,#3f5a3b 0%,#6f8a5a 35%,#a7a08a 60%,#d9c8b5 80%,#b9a58e 100%)}
.hero-rule{position:absolute;left:190px;top:168px;width:320px;height:1px;background:rgba(255,255,255,.8)}
.hero h1{position:absolute;left:0;width:696px;text-align:center;color:var(--white);font-size:64px;line-height:1;letter-spacing:-1px}
.hero .line-one{top:218px;font-weight:700}
.hero .line-two{top:296px;font-weight:300}

.welcome{position:absolute;top:770px;left:0;width:1200px;height:500px}
.welcome-image{position:absolute;left:78px;top:75px;width:466px;height:268px;border-radius:8px;background:linear-gradient(135deg,#d9d4cc 0%,#b7d6cb 55%,#8fa89e 100%)}
.section-title{font-size:41px;color:var(--ink);font-weight:400}
.section-title b{font-weight:700}
.welcome p{position:absolute;left:623px;top:178px;width:480px;font-size:16.5px;line-height:28.3px;color:var(--muted)}

.services{position:absolute;top:1270px;left:0;width:1200px;height:1052px;background:var(--soft-bg)}
.centered{position:absolute;left:0;width:1200px;text-align:center}
.service-card{position:absolute;width:304px;height:328px;border-radius:10px;overflow:hidden}
.service-card .label{position:absolute;left:0;top:244px;width:100%;height:54px;background:rgba(255,255,255,.62);display:flex;align-items:center;justify-content:center;font-size:22px;color:var(--ink)}

.testimonials{position:absolute;top:2322px;left:0;width:1200px;height:526px}
.quote{position:absolute;left:240px;top:200px;width:720px;text-align:center;font-style:italic;font-size:20.5px;line-height:33px;color:#555}
.arrow{position:absolute;width:22px;height:30px;stroke:#666;stroke-width:2.5;fill:none}
.avatar{position:absolute;left:513px;top:386px;width:84px;height:84px;border-radius:50%;background:#ddd;overflow:hidden}
.client-name{position:absolute;left:616px;top:414px;font-size:22px;color:#555}

.cta{position:absolute;top:2848px;left:0;width:1200px;height:270px;background:linear-gradient(90deg,#b9dccd 0%,#a6d1bf 45%,#8fb7a6 75%,#a5cdbd 100%)}
.cta h2{position:absolute;left:0;top:62px;width:1200px;text-align:center;color:var(--white);font-size:39px;font-weight:700}

.blog{position:absolute;top:3118px;left:0;width:1200px;height:683px}
.post{position:absolute;top:191px;width:312px}
.post .thumb{width:312px;height:216px;border-radius:8px}
.post h3{margin-top:22px;font-size:22px;font-weight:400;color:var(--ink)}
.post .meta{margin-top:9px;font-size:15.5px;color:#666;display:flex;align-items:center;gap:5px}
.post .meta svg{width:13px;height:13px;fill:#d9ccb9}
.post p{margin-top:16px;font-size:16px;line-height:24px;color:var(--muted)}
.post .more{display:block;margin-top:14px;font-size:16px;color:var(--mint);text-transform:uppercase}

.site-footer{position:absolute;top:3801px;left:0;width:1200px;height:413px;background:var(--footer);color:var(--white)}
.site-footer .brand{color:var(--white);top:62px}
.site-footer h4{position:absolute;font-size:20px;font-weight:700}
.footer-links{position:absolute;left:495px;top:100px;list-style:none;font-size:16.5px;line-height:31px}
.contact-list{position:absolute;left:728px;top:100px;font-size:16.5px;line-height:31px}
.contact-list svg{width:13px;height:13px;fill:var(--white);vertical-align:-1px;margin-right:9px}
.footer-rule{position:absolute;left:111px;top:314px;width:978px;height:1px;background:#555}
.copyright{position:absolute;left:111px;top:348px;font-size:16.5px}
.social{position:absolute;top:339px;width:36px;height:36px;border-radius:50%;border:1.5px solid #bbb}
</style>
</head>
<body>

<div class="top-bar">
  <span><svg viewBox="0 0 24 24"><path d="M6.6 10.8a15 15 0 006.6 6.6l2.2-2.2c.3-.3.7-.4 1-.2 1.1.4 2.3.6 3.6.6.6 0 1 .4 1 1V20c0 .6-.4 1-1 1A17 17 0 013 4c0-.6.4-1 1-1h3.5c.6 0 1 .4 1 1 0 1.3.2 2.5.6 3.6.1.3 0 .7-.2 1z"/></svg>1 555 010 2040</span>
  <span>|</span>
  <span><svg viewBox="0 0 24 24"><path d="M2 5h20v2l-10 6L2 7zM2 9l10 6 10-6v10H2z"/></svg>info@velmoraMD.com</span>
</div>

<header class="site-header">
  <div class="brand">VelmoraMD.</div>
  <nav class="main-nav">
    <span class="current">Home</span><span>About</span><span>Services</span><span>Plans</span><span>Blog</span><span>Contact</span>
  </nav>
  <div class="btn-outline" style="left:898px;top:31px;width:189px;height:51px;font-weight:700;font-size:16px">Become a Provider</div>
</header>

<section class="hero" role="img" aria-label="Woman in a white shirt smiling, seated among green tropical plants">
  <div class="hero-rule"></div>
  <h1 class="line-one">LOOK AND FEEL</h1>
  <h1 class="line-two">YOUR BEST</h1>
  <div class="btn-white" style="left:214px;top:393px;width:272px;height:64px">Request Consultation</div>
</section>

<section class="welcome">
  <div class="welcome-image" role="img" aria-label="Photo of a white vase with dried leaves and skincare serum bottles"></div>
  <div class="accent-bar" style="left:623px;top:82px"></div>
  <h2 class="section-title abs" style="left:623px;top:106px"><b>Welcome to</b> VelmoraMD</h2>
  <p>Lorem ipsum dolor sit amet, consectetur adipiscing elit, sed do eiu smod tempor incididunt ut labore et dolore magna aliqua. Ut enim ad minim veniam, quis nostrud exercitation ullamco laboris nisi ut aliquip ex ea commodo consequat. Duis aute re dolor in repreh nderit in voluptate velit esse cillum dolore eu fugiat nulla parisileh jaturce pteur.</p>
  <div class="btn-outline" style="left:623px;top:384px;width:152px;height:54px">Read More</div>
</section>

<section class="services">
  <div class="accent-bar" style="left:578px;top:56px"></div>
  <h2 class="section-title centered" style="top:86px"><b>Our</b> Services</h2>

  <div class="service-card" style="left:111px;top:179px;background:linear-gradient(160deg,#e6e2df,#d7b8a5 60%,#b18a74)" role="img" aria-label="Injection treatment near the lips"><div class="label">Botox parties</div></div>
  <div class="service-card" style="left:448px;top:179px;background:linear-gradient(160deg,#ecece9,#cfc5bb 55%,#7d7873)" role="img" aria-label="Clinician applying filler to a male client"><div class="label">Dermal Fillers</div></div>
  <div class="service-card" style="left:785px;top:179px;background:linear-gradient(160deg,#d6e6e4,#eae7e2 55%,#6b9aa3)" role="img" aria-label="Woman seated in a treatment chair"><div class="label">IV therapy</div></div>

  <div class="service-card" style="left:111px;top:540px;background:linear-gradient(160deg,#cfd4d6,#8fa3a6 50%,#1f9b8f)" role="img" aria-label="Older man receiving a device treatment"><div class="label">ED</div></div>
  <div class="service-card" style="left:448px;top:540px;background:linear-gradient(160deg,#d8d6d3,#d9b9a3 55%,#c9cfd6)" role="img" aria-label="Mature woman touching her neck"><div class="label">BHRT</div></div>
  <div class="service-card" style="left:785px;top:540px;background:linear-gradient(160deg,#e3e3e3,#f0dfd3 55%,#c8a48d)" role="img" aria-label="Woman receiving a facial device treatment"><div class="label">Peptides</div></div>

  <div class="btn-outline" style="left:523px;top:923px;width:152px;height:54px">View More</div>
</section>

<section class="testimonials">
  <div class="accent-bar" style="left:578px;top:72px"></div>
  <h2 class="section-title centered" style="top:106px"><b>Client</b> Testimonials</h2>
  <svg class="arrow" style="left:170px;top:253px" viewBox="0 0 22 30"><path d="M16 4 L6 15 L16 26"/></svg>
  <svg class="arrow" style="left:1003px;top:253px" viewBox="0 0 22 30"><path d="M6 4 L16 15 L6 26"/></svg>
  <p class="quote">“ Lorem ipsum dolor sit amet, consectetur apiscing elit, sed do eiusmod tempor inc ididunt ut labore et dolore magna aliqua. Ut enim ad minim veniam, quis nostrud exercitation ullamco laboris nisi ut aliquip ex ea commi odo consequat. Duis aute irure dolor in reprehenderit in voluptate sse vcillum dolore ”</p>
  <div class="avatar" aria-label="Default profile placeholder">
    <svg viewBox="0 0 84 84" width="84" height="84"><circle cx="42" cy="32" r="16" fill="#fff"/><path d="M12 84 C14 58 70 58 72 84Z" fill="#fff"/></svg>
  </div>
  <div class="client-name">Morgan</div>
</section>

<section class="cta" role="img" aria-label="Mint-tinted photo of a woman in profile receiving a facial treatment">
  <h2>We are More than a clinic, Join our community</h2>
  <div class="btn-white" style="left:464px;top:139px;width:272px;height:64px">Request Consultation</div>
</section>

<section class="blog">
  <div class="accent-bar" style="left:578px;top:70px"></div>
  <h2 class="section-title centered" style="top:106px"><b>Latest</b> Blog</h2>

  <article class="post" style="left:111px">
    <div class="thumb" style="background:linear-gradient(135deg,#f3f1ee,#d8cfc3 55%,#9a8b7a)" role="img" aria-label="White vase with dried leaves beside serum bottles"></div>
    <h3>Finibus Bonoruet Malorum</h3>
    <div class="meta"><svg viewBox="0 0 12 12"><rect x="0" y="2" width="12" height="10" rx="1"/></svg>25/05/2022 | <svg viewBox="0 0 12 12"><circle cx="6" cy="3.5" r="3"/><path d="M0 12c0-4 12-4 12 0z"/></svg>Admin</div>
    <p>Duis aute irure dolor in reprehenderit in voluptate velit esse cillum dolore eu fugiat nulla pariatur.</p>
    <span class="more">Read More</span>
  </article>

  <article class="post" style="left:445px">
    <div class="thumb" style="background:linear-gradient(135deg,#e8f0ea,#8fc7a8 50%,#4d8f6d)" role="img" aria-label="Woman posing against a green patterned wall"></div>
    <h3>Finibus Bonoruet Malorum</h3>
    <div class="meta"><svg viewBox="0 0 12 12"><rect x="0" y="2" width="12" height="10" rx="1"/></svg>25/05/2022 | <svg viewBox="0 0 12 12"><circle cx="6" cy="3.5" r="3"/><path d="M0 12c0-4 12-4 12 0z"/></svg>Admin</div>
    <p>Duis aute irure dolor in reprehenderit in voluptate velit esse cillum dolore eu fugiat nulla pariatur.</p>
    <span class="more">Read More</span>
  </article>

  <article class="post" style="left:777px">
    <div class="thumb" style="background:linear-gradient(135deg,#f4f2ee,#e6ded3 55%,#c9b9a6)" role="img" aria-label="Clinician in a white coat standing in a bright room"></div>
    <h3>Finibus Bonoruet Malorum</h3>
    <div class="meta"><svg viewBox="0 0 12 12"><rect x="0" y="2" width="12" height="10" rx="1"/></svg>25/05/2022 | <svg viewBox="0 0 12 12"><circle cx="6" cy="3.5" r="3"/><path d="M0 12c0-4 12-4 12 0z"/></svg>Admin</div>
    <p>Duis aute irure dolor in reprehenderit in voluptate velit esse cillum dolore eu fugiat nulla pariatur.</p>
    <span class="more">Read More</span>
  </article>
</section>

<footer class="site-footer">
  <div class="brand">VelmoraMD.</div>
  <h4 style="left:495px;top:56px">Quick Links</h4>
  <ul class="footer-links">
    <li>Home</li><li>About</li><li>Services</li><li>Plans</li><li>Blog</li><li>Contact</li>
  </ul>
  <h4 style="left:728px;top:56px">Contact Us</h4>
  <div class="contact-list">
    <div><svg viewBox="0 0 24 24"><path d="M6.6 10.8a15 15 0 006.6 6.6l2.2-2.2c.3-.3.7-.4 1-.2 1.1.4 2.3.6 3.6.6.6 0 1 .4 1 1V20c0 .6-.4 1-1 1A17 17 0 013 4c0-.6.4-1 1-1h3.5c.6 0 1 .4 1 1 0 1.3.2 2.5.6 3.6.1.3 0 .7-.2 1z"/></svg>1 555 010 2040</div>
    <div style="margin-top:18px"><svg viewBox="0 0 24 24"><path d="M2 5h20v2l-10 6L2 7zM2 9l10 6 10-6v10H2z"/></svg>info@velmoraMD.com</div>
    <div style="margin-top:24px"><svg viewBox="0 0 24 24"><path d="M12 2a7 7 0 00-7 7c0 5 7 13 7 13s7-8 7-13a7 7 0 00-7-7zm0 9.5A2.5 2.5 0 1112 6.5a2.5 2.5 0 010 5z"/></svg>4820 Alder Rd Suite 2</div>
    <div style="padding-left:22px">Ashvale OR 97000</div>
  </div>
  <div class="footer-rule"></div>
  <div class="copyright">©2022, velmoraMD. All rights reserved.</div>
  <div class="social" style="left:1004px" aria-label="Social profile"></div>
  <div class="social" style="left:1050px" aria-label="Social profile"></div>
</footer>

</body>
</html>
```